Stonebrook 720 Real Estate Investment Company

We need a business card designed for a real estate investment company named Stonebrook 720. We want to use red#f04a50, orange #f37122 and yellow #fbee3e as the color scheme. The logo colors will need to be modified from the current blue palette. I've attach VitaPathway logo example that captures the color scheme we're going for for Stonebrook 720. Looking for clean Sans Serif fonts.
Contact Information for Business Card
Daniel Furlow
Managing Partner
48317 Whitfield Lane, Suite 510
Tampa, FL 33718
813-555-4870 Mobile
dfurlow@stonebrook720.example
www.stonebrook720.example
Requirements
Must have
- Looking for creative responses.
Nice to have
- Must hit color palette... orange, red, yellow

```html
<!DOCTYPE html>
<html lang="en">
<head>
<meta charset="utf-8">
<title>Stonebrook 720 — Business Card</title>
<link rel="stylesheet" href="https://fonts.googleapis.com/css2?family=Fira+Sans:wght@400;500;600;700&display=swap">
<style>
  :root {
    --backdrop: #2b2d31;
    --card-white: #ffffff;
    --ink: #1a1a1a;
    --ink-soft: #333538;
    --brand-red: #f04a50;
    --brand-orange: #f37122;
    --brand-yellow: #fbee3e;
    --deco-light: #fff3d6;
    --deco-mid: #f9b48a;
  }
  * { margin: 0; padding: 0; box-sizing: border-box; }
  html, body {
    width: 1200px;
    height: 960px;
    overflow: hidden;
    background: var(--backdrop);
    font-family: "Fira Sans", Arial, sans-serif;
  }
  .stage {
    position: relative;
    width: 1200px;
    height: 960px;
    display: flex;
    align-items: center;
    justify-content: center;
    gap: 56px;
  }
  .card {
    position: relative;
    width: 530px;
    height: 303px;
    border-radius: 4px;
    overflow: hidden;
    box-shadow: 0 10px 28px rgba(0,0,0,0.45);
  }

  /* Front */
  .card-front { background: var(--card-white); }
  .brand-decoration {
    position: absolute;
    left: 0;
    top: 0;
    width: 220px;
    height: 100%;
    background: linear-gradient(135deg, var(--deco-light) 0%, var(--deco-mid) 100%);
  }
  .front-info {
    position: absolute;
    left: 262px;
    top: 44px;
    color: var(--ink-soft);
  }
  .wordmark {
    display: flex;
    align-items: center;
    gap: 10px;
    font-weight: 700;
    font-size: 31px;
    letter-spacing: -0.5px;
    color: var(--ink);
    margin-bottom: 22px;
  }
  .wordmark-dot {
    width: 14px;
    height: 14px;
    border-radius: 50%;
    background: var(--brand-orange);
    flex: none;
  }
  .person-name {
    font-size: 19px;
    font-weight: 500;
    color: var(--brand-red);
    line-height: 1.1;
  }
  .person-title {
    font-size: 12px;
    margin-bottom: 10px;
  }
  .contact-list { list-style: none; font-size: 12px; line-height: 1.6; }
  .contact-list li { display: flex; align-items: center; gap: 8px; }
  .contact-list svg { width: 11px; height: 11px; flex: none; fill: var(--brand-orange); }
  .address { font-size: 12px; line-height: 1.5; margin-top: 6px; font-style: normal; }

  /* Back */
  .card-back {
    background: linear-gradient(160deg, var(--brand-orange) 0%, var(--brand-red) 100%);
    display: flex;
    align-items: center;
    justify-content: center;
  }
  .card-back .wordmark {
    color: #ffffff;
    font-size: 38px;
    margin: 0;
  }
  .card-back .wordmark-dot { background: var(--brand-yellow); width: 16px; height: 16px; }
</style>
</head>
<body>
<main class="stage">

  <section class="card card-front" aria-label="Business card front">
    <div class="brand-decoration" role="img" aria-label="Large brand decoration in warm orange and red tones"></div>
    <div class="front-info">
      <div class="wordmark"><span>Stonebrook720</span><span class="wordmark-dot"></span></div>
      <p class="person-name">Daniel Furlow</p>
      <p class="person-title">Managing Partner</p>
      <ul class="contact-list">
        <li>
          <svg viewBox="0 0 24 24" aria-hidden="true"><path d="M6.6 10.8a15.1 15.1 0 0 0 6.6 6.6l2.2-2.2c.3-.3.7-.4 1-.2 1.1.4 2.3.6 3.6.6.6 0 1 .4 1 1V20c0 .6-.4 1-1 1A17 17 0 0 1 3 4c0-.6.4-1 1-1h3.5c.6 0 1 .4 1 1 0 1.3.2 2.5.6 3.6.1.3 0 .7-.2 1z"/></svg>
          813-555-4870
        </li>
        <li>
          <svg viewBox="0 0 24 24" aria-hidden="true"><path d="M2 5h20v14H2zM4 7v.5l8 5 8-5V7l-8 5z"/></svg>
          dfurlow@stonebrook720.example
        </li>
        <li>
          <svg viewBox="0 0 24 24" aria-hidden="true"><path d="M12 2a10 10 0 1 0 0 20 10 10 0 0 0 0-20zm0 2c.9 0 2.2 1.8 2.8 5H9.2C9.8 5.8 11.1 4 12 4zM4.3 11h4.6c0 .7 0 1.4.1 2H4.3a8 8 0 0 1 0-2zm.7 4h4.3c.4 2 1 3.5 1.7 4.6A8 8 0 0 1 5 15zm4.3-6H5a8 8 0 0 1 6-4.6C10.3 5.5 9.7 7 9.3 9zm1.7 4a18 18 0 0 1 0-2h2a18 18 0 0 1 0 2zm1 7c-.9 0-2.2-1.8-2.8-5h5.6c-.6 3.2-1.9 5-2.8 5zm1-.4c.7-1.1 1.3-2.6 1.7-4.6H19a8 8 0 0 1-6 4.6zm2-6.6c.1-.6.1-1.3.1-2h4.6a8 8 0 0 1 0 2zm-.3-4c-.4-2-1-3.5-1.7-4.6A8 8 0 0 1 19 9z"/></svg>
          www.stonebrook720.example
        </li>
      </ul>
      <address class="address">48317 Whitfield Lane,<br>Suite 510, Tampa, FL 33718</address>
    </div>
  </section>

  <section class="card card-back" aria-label="Business card back">
    <div class="wordmark"><span>Stonebrook720</span><span class="wordmark-dot"></span></div>
  </section>

</main>
</body>
</html>
```